Custom Business Card Design

We are looking for a raised spot logo design to use with Tavu.com. We will provide the logo files. Should be a front and back design. We want to implement the house into the back design using the same colors as the logo through out. Something VERY cool!

```html
<!DOCTYPE html>
<html lang="en">
<head>
<meta charset="utf-8">
<title>Tavu.com Business Card</title>
<link rel="stylesheet" href="https://fonts.googleapis.com/css2?family=Open+Sans:wght@400;600&display=swap">
<style>
  :root {
    --stage: #000000;
    --card-dark: #231f20;
    --brand-blue: #2f7fc4;
    --soft-blue: #5b9dd6;
    --deep-blue: #4a8bcc;
    --light-blue: #79b2e3;
    --text-light: #e9e9e9;
    --white: #ffffff;
  }
  * { margin: 0; padding: 0; box-sizing: border-box; }
  html, body {
    width: 1200px;
    height: 900px;
    overflow: hidden;
    background: var(--stage);
    font-family: "Open Sans", Arial, sans-serif;
  }
  .stage { position: relative; width: 1200px; height: 900px; }

  .card {
    position: absolute;
    top: 275px;
    width: 477px;
    height: 294px;
    overflow: hidden;
  }
  .card-front {
    left: 116px;
    background: var(--card-dark);
    border-radius: 0 52px 0 52px;
    color: var(--text-light);
  }
  .card-back {
    left: 622px;
    border-radius: 52px 0 52px 0;
  }

  /* Front: brand block */
  .brand {
    position: absolute;
    left: 200px;
    top: 81px;
    width: 250px;
    text-align: center;
  }
  .brand-rule { height: 1.5px; background: var(--brand-blue); }
  .brand-name {
    font-size: 31px;
    font-weight: 600;
    color: var(--brand-blue);
    line-height: 43px;
    letter-spacing: 0.5px;
  }

  /* Front: person */
  .person-name {
    position: absolute;
    left: 23px;
    top: 159px;
    font-size: 20px;
    font-weight: 400;
    color: var(--brand-blue);
    line-height: 26px;
  }
  .person-rule {
    position: absolute;
    left: 188px;
    top: 173px;
    width: 263px;
    height: 1px;
    background: var(--brand-blue);
  }
  .person-title {
    position: absolute;
    left: 23px;
    top: 183px;
    font-size: 12.5px;
  }

  .address {
    position: absolute;
    left: 23px;
    top: 236px;
    font-size: 12.5px;
    line-height: 17px;
  }

  .contacts {
    position: absolute;
    right: 24px;
    top: 203px;
    list-style: none;
    font-size: 12.5px;
    line-height: 17px;
    text-align: right;
  }
  .contacts li { display: flex; justify-content: flex-end; align-items: center; gap: 5px; }
  .contacts svg { width: 10px; height: 10px; fill: var(--soft-blue); flex: none; }

  /* Back */
  .back-art { position: absolute; inset: 0; }
  .back-brand {
    position: absolute;
    left: 0;
    right: 0;
    top: 118px;
    display: flex;
    justify-content: center;
    align-items: center;
    gap: 14px;
    color: var(--white);
    font-size: 44px;
    font-weight: 600;
    line-height: 60px;
  }
  .back-brand .dot {
    width: 26px; height: 26px;
    border-radius: 50%;
    background: var(--white);
  }
  .social {
    position: absolute;
    top: 249px;
    left: 0; right: 0;
    display: flex;
    justify-content: center;
    gap: 9px;
    list-style: none;
  }
  .social li {
    width: 25px; height: 25px;
    border-radius: 50%;
    background: var(--white);
  }
</style>
</head>
<body>
<main class="stage">

  <section class="card card-front" aria-label="Card front">
    <div class="brand">
      <div class="brand-rule"></div>
      <div class="brand-name">Tavu.com</div>
      <div class="brand-rule"></div>
    </div>

    <h1 class="person-name">Daniel Hart</h1>
    <div class="person-rule"></div>
    <p class="person-title">Managing Director</p>

    <p class="address">12345, Address Goes Here<br>Country Name, 123456.</p>

    <ul class="contacts">
      <li>044-123 456 789
        <svg viewBox="0 0 10 10" aria-hidden="true"><path d="M2.5 0h5a1 1 0 0 1 1 1v8a1 1 0 0 1-1 1h-5a1 1 0 0 1-1-1V1a1 1 0 0 1 1-1zm.4 1.2v6.4h4.2V1.2z"/></svg>
      </li>
      <li>044-123 456 789
        <svg viewBox="0 0 10 10" aria-hidden="true"><path d="M0 3.5C1 1.5 9 1.5 10 3.5v1H7.5V3.3h-5v1.2H0zM2 5h6l1.5 4h-9z"/></svg>
      </li>
      <li>info@webname.com
        <svg viewBox="0 0 10 10" aria-hidden="true"><path d="M0 2h10v6H0zm1 .8 4 3 4-3z"/></svg>
      </li>
      <li>www.websitename.com
        <svg viewBox="0 0 10 10" aria-hidden="true"><circle cx="5" cy="5" r="5"/><path d="M0 5h10M5 0c-2.5 2.5-2.5 7.5 0 10M5 0c2.5 2.5 2.5 7.5 0 10" stroke="#231f20" stroke-width="0.7" fill="none"/></svg>
      </li>
    </ul>
  </section>

  <section class="card card-back" aria-label="Card back">
    <svg class="back-art" viewBox="0 0 477 294" preserveAspectRatio="none" role="img" aria-label="Layered blue background with faint angled light bands">
      <defs>
        <linearGradient id="backGlow" x1="0" y1="0" x2="1" y2="1">
          <stop offset="0" stop-color="#5a9bd5"/>
          <stop offset="0.5" stop-color="#69a7dd"/>
          <stop offset="1" stop-color="#4a8acb"/>
        </linearGradient>
        <radialGradient id="centerLight" cx="0.5" cy="0.5" r="0.5">
          <stop offset="0" stop-color="#ffffff" stop-opacity="0.22"/>
          <stop offset="1" stop-color="#ffffff" stop-opacity="0"/>
        </radialGradient>
      </defs>
      <rect width="477" height="294" fill="url(#backGlow)"/>
      <polygon points="0,150 150,0 230,0 0,230" fill="#ffffff" opacity="0.08"/>
      <polygon points="0,294 294,0 330,0 36,294" fill="#ffffff" opacity="0.07"/>
      <polygon points="160,294 454,0 477,0 477,40 223,294" fill="#2f6fb2" opacity="0.12"/>
      <polygon points="300,294 477,117 477,200 383,294" fill="#ffffff" opacity="0.09"/>
      <rect x="0" y="0" width="477" height="294" fill="url(#centerLight)"/>
      <line x1="40" y1="218" x2="437" y2="218" stroke="#ffffff" stroke-opacity="0.45" stroke-width="1"/>
      <line x1="40" y1="76" x2="437" y2="76" stroke="#ffffff" stroke-opacity="0.45" stroke-width="1"/>
    </svg>

    <div class="back-brand"><span class="dot"></span>Tavu.com</div>

    <ul class="social" aria-label="Social links">
      <li></li><li></li><li></li>
    </ul>
  </section>

</main>
</body>
</html>
```